TalkWell needs a Letterhead

We need a letterhead for our company "TalkWell Consultants". Logo is attached. The company color is Turquoise. Icons for website, scan logo for website, icons for address, e-mail and phone appreciated rather than just words.

```html
<!DOCTYPE html>
<html lang="en">
<head>
<meta charset="utf-8">
<title>TalkWell Consultants – Letterhead</title>
<link rel="stylesheet" href="https://fonts.googleapis.com/css2?family=Open+Sans:wght@400;600&display=swap">
<style>
  :root {
    --brand-blue: #3f5aa8;
    --brand-blue-light: #5c78c4;
    --brand-green: #8cc63f;
    --logo-blue: #2b78c4;
    --ink: #1f1f1f;
    --paper: #ffffff;
    --backdrop: #e9e9ea;
  }
  * { box-sizing: border-box; margin: 0; padding: 0; }
  html, body {
    width: 1200px; height: 1000px; overflow: hidden;
    background: var(--backdrop);
    font-family: "Open Sans", Arial, sans-serif;
  }
  .letterhead {
    position: absolute; left: 282px; top: 40px;
    width: 636px; height: 920px;
    background: var(--paper);
    box-shadow: 0 2px 10px rgba(0,0,0,.12);
    overflow: hidden;
  }
  .header-band { position: absolute; left: 0; top: 0; width: 636px; height: 90px; }
  .brand {
    position: absolute; left: 40px; top: 100px;
    display: flex; align-items: center; gap: 10px;
  }
  .brand-mark { width: 26px; height: 26px; background: var(--logo-blue); }
  .brand-name { font-size: 24px; font-weight: 400; color: var(--logo-blue); line-height: 1; }
  .brand-sub { font-size: 9px; letter-spacing: 3px; color: var(--logo-blue); margin-top: 3px; }
  .contact {
    position: absolute; right: 36px; top: 98px;
    list-style: none; font-size: 10px; color: var(--ink); line-height: 17px;
  }
  .contact li { display: flex; align-items: center; justify-content: flex-end; gap: 8px; }
  .contact svg { width: 12px; height: 12px; flex: none; }
  .letter-body {
    position: absolute; left: 52px; top: 200px; width: 530px;
    font-size: 11.5px; line-height: 17px; color: var(--ink);
  }
  .letter-body p { margin-bottom: 14px; }
</style>
</head>
<body>
  <div class="letterhead">
    <svg class="header-band" viewBox="0 0 636 90" aria-hidden="true">
      <path d="M0 0 H636 V62 Q330 40 0 20 Z" fill="var(--brand-green)"/>
      <path d="M0 0 H636 V54 Q330 32 0 14 Z" fill="var(--brand-blue)"/>
      <path d="M470 0 H560 L610 46 Q560 42 520 40 Z" fill="var(--brand-blue-light)" opacity=".55"/>
    </svg>

    <div class="brand">
      <span class="brand-mark"></span>
      <div>
        <div class="brand-name">TalkWell</div>
        <div class="brand-sub">CONSULTANTS</div>
      </div>
    </div>

    <ul class="contact">
      <li>Quidam persecuti ut sed<br>maiorum propriae nec ex
        <svg viewBox="0 0 12 12"><path d="M6 1 1 5.5V11h4V8h2v3h4V5.5Z" fill="var(--brand-green)"/></svg></li>
      <li>www.talkwellconsult.com
        <svg viewBox="0 0 12 12"><circle cx="6" cy="6" r="5" fill="none" stroke="var(--brand-blue)" stroke-width="1.2"/><path d="M1 6h10M6 1c-3 3-3 7 0 10M6 1c3 3 3 7 0 10" fill="none" stroke="var(--brand-blue)" stroke-width=".9"/></svg></li>
      <li>hello@talkwellconsult.com
        <svg viewBox="0 0 12 12"><circle cx="6" cy="6" r="2.2" fill="none" stroke="var(--brand-green)" stroke-width="1.4"/><path d="M8.2 4v3c0 1.5 2.8 1.5 2.8-1A5 5 0 1 0 8.5 10.3" fill="none" stroke="var(--brand-green)" stroke-width="1.4"/></svg></li>
      <li>#0000 000 000
        <svg viewBox="0 0 12 12"><path d="M3 1h2l1 3-1.5 1a6 6 0 0 0 2.5 2.5L8 6l3 1v2c0 1-1 2-2 2A8 8 0 0 1 1 3c0-1 1-2 2-2Z" fill="var(--brand-blue)"/></svg></li>
    </ul>

    <div class="letter-body">
      <p>Lorem ipsum dolor sit amet, sea ex scripta molestiae. No cum omnis congue, pro in augue civibus concludaturque, has habeo quando at. Cu his causae aliquid deserunt, dignissim neglegentur pri cu. Essent adolescens usu te, ut ullum graeco duo, vim ad meis adhuc. Inani delicatissimi at quo, nec et nullam prompta habemus. Hinc graeco perpetua quo te, meis habeo incorrupte eu nam.</p>
      <p>Quidam persecuti ut sed, maiorum propriae nec ex. Augue delenit tincidunt has id. Delicata salutandi vim ne, ea eam expetendis assueverit definitiones, has et labores facilisi deseruisse. Sale consequat assueverit per at. Omnes omnium lobortis te mea.</p>
      <p>His ubique animal molestie ut. Sit an nostro argumentum. Sit doming tritani saperet te. In omnesque similique vis, quaerendum persequeris eu sea. Soluta disputando ex mel, ea pri dicit perpetua dissentias. Ei mea nemore phaedrum scriptorem.Lorem ipsum dolor sit amet, sea ex scripta molestiae. No cum omnis congue, pro in augue civibus concludaturque, has habeo quando at. Cu his causae aliquid deserunt, dignissim neglegentur pri cu. Essent adolescens usu te, ut ullum graeco duo, vim ad meis adhuc. Inani delicatissimi at quo, nec et nullam prompta habemus. Hinc graeco perpetua quo te, meis habeo incorrupte eu nam.</p>
      <p>Quidam persecuti ut sed, maiorum propriae nec ex. Augue delenit tincidunt has id. Delicata salutandi vim ne, ea eam expetendis assueverit definitiones, has et labores facilisi deseruisse. Sale consequat assueverit per at. Omnes omnium lobortis te mea.</p>
      <p>His ubique animal molestie ut. Sit an nostro argumentum. Sit doming tritani saperet te. In omnesque similique vis, quaerendum persequeris eu sea. Soluta disputando ex mel, ea pri dicit perpetua dissentias. Ei mea nemore phaedrum scriptorem His ubique animal molestie ut. Sit an nostro argumentum. Sit doming tritani saperet te. In omnesque similique vis, quaerendum persequeris eu sea. Soluta disputando ex mel, ea pri dicit perpetua dissentias. Ei mea nemore phaedrum scriptorem.</p>
    </div>
  </div>
</body>
</html>
```